Australian Grown Coffee needs a premium, OUTSTANDING!! Coffee bag design

Morrell coffee is a family owned and run company with coffee being in our blood, currently being run by 3rd gen coffee farmers with roots tying back to coffee growing in Tanzania. We grow, process and roast a very high quality Arabica Coffee (It has won the Gold/ The best milk based coffee in Australia at the silver kettle prizes in the past). We package our coffee beans and ground coffee into 1kg and 250gram bags, which are a bit dated now. We would love to get some amazing designs to bring our product into the future. Our target audience would be 25yrs- 60yr old with a large proportion coming to our plantation to do a tour enjoy a cup, take home a momento and then turn into an online customer.
Content
We would like to achieve a modern standout packaging design that reflects our premium quality Australian coffee. We have a medium roast and an espresso roast lines that we grow roast and sell.
We are happy to see designs that are creative and unique, not just another coffee bag on the shelf, but a standout premium product, that reflects that the coffee is actually grown in Australia, not just roasted here.
Our current colours are red and gold, and we are looking to package our coffee in box bottom bags with rippa zippas with both the 1kg and 250 gram lines, but are open to any other fantastic packaging concepts too.
The bag need to communicate the high quality of the bean within.
Some brainstormed keywords are: Australian, Fresh, Single Origin, Premium, Reserve, Cafe, Barista, Very High Quality, Grown, Plantation.

Target Market(s)

The target market is 25yrs+

Industry/Entity Type

It Company

Font styles to use
Sans Serif
Script

Colors
ec1f27
ffffff
ffc214
0792cd
9bcb3c

Requirements
Must have
• A unique design that stands out from all the rest, ie I'll buy this one! It is more expensive but the package looks so premium i don't mind paying extra for it.
• -Name of roast:(Espresso Roast, Beans), (Espresso Roast, Fine Grind), (Medium Roast beans), ( Medium roast, Plunger/Drip Grind).
• - An area on the back of the package for a barcode Ean13.
Nice to have
• Class added, either in a fancy emblem (think Australian nation emblem except better :)
• Something really attractive in the side gussets
• Clear and concise, uncluttered.
Should not have
• Just a picture of a kangaroo/ koala...

```html
<!DOCTYPE html>
<html lang="en">
<head>
<meta charset="utf-8">
<title>Morrell Coffee – Espresso Roast Beans Bag</title>
<link rel="stylesheet" href="https://fonts.googleapis.com/css2?family=Cinzel:wght@400;600&family=Open+Sans:wght@600;700&family=Oswald:wght@400;500&display=swap">
<style>
  :root {
    --page-bg: #ebe5de;
    --copper-dark: #8f5235;
    --copper-mid: #b5683f;
    --copper-light: #d88b5c;
    --ink-white: #ffffff;
    --ink-dark: #2b2126;
    --band-beige: #b7a88c;
    --ring-beige: #cbbfa6;
    --scene-brown: #7a4a31;
    --scene-brown-light: #9a5f3f;
    --ribbon: #2b2126;
  }
  html, body {
    margin: 0;
    width: 1200px;
    height: 1123px;
    overflow: hidden;
    background: var(--page-bg);
  }
  .canvas {
    position: relative;
    width: 1200px;
    height: 1123px;
  }
  .bag {
    position: absolute;
    left: 365px;
    top: 40px;
    width: 470px;
    height: 1043px;
    border-radius: 10px;
    overflow: hidden;
    background:
      linear-gradient(90deg, rgba(255,255,255,0) 0%, rgba(255,210,170,0.25) 45%, rgba(255,255,255,0) 60%),
      linear-gradient(180deg, var(--copper-light) 0%, var(--copper-mid) 40%, var(--copper-dark) 100%);
    box-shadow: 0 6px 20px rgba(0,0,0,0.2);
    font-family: "Open Sans", sans-serif;
    color: var(--ink-white);
  }
  .seal-lines {
    position: absolute;
    left: 35px;
    top: 100px;
    width: 389px;
  }
  .seal-lines span {
    display: block;
    height: 10px;
    border: 1.5px solid rgba(60,30,20,0.45);
    margin-bottom: 12px;
  }
  .brand {
    position: absolute;
    left: 0;
    top: 225px;
    width: 100%;
    text-align: center;
  }
  .brand-name {
    font-family: "Cinzel", serif;
    font-weight: 400;
    font-size: 56px;
    letter-spacing: 2px;
    line-height: 1;
    margin: 0;
  }
  .brand-tagline {
    font-weight: 700;
    font-size: 29px;
    margin: 14px 0 0;
    letter-spacing: 0.5px;
  }
  .roast-name {
    position: absolute;
    top: 352px;
    width: 100%;
    text-align: center;
    font-family: "Cinzel", serif;
    font-weight: 600;
    color: var(--ink-dark);
  }
  .roast-name .line {
    display: block;
    font-size: 30px;
    line-height: 1.1;
    letter-spacing: 1px;
  }
  .roast-name .form {
    display: block;
    font-size: 20px;
    margin-top: 2px;
  }
  .roast-level {
    position: absolute;
    left: 97px;
    top: 448px;
    width: 278px;
    height: 26px;
    background: var(--band-beige);
    font-family: "Cinzel", serif;
    font-size: 15px;
    letter-spacing: 1px;
    text-align: center;
    line-height: 26px;
  }
  .rule {
    position: absolute;
    left: 97px;
    width: 278px;
    background: var(--ink-dark);
  }
  .rule.one { top: 489px; height: 4px; }
  .rule.two { top: 500px; height: 4px; }
  .origin {
    position: absolute;
    top: 528px;
    width: 100%;
    text-align: center;
    font-family: "Oswald", sans-serif;
  }
  .origin-label {
    display: block;
    font-weight: 500;
    font-size: 23px;
    letter-spacing: 1.5px;
    color: var(--ink-dark);
  }
  .origin-country {
    display: block;
    font-weight: 500;
    font-size: 68px;
    letter-spacing: 2px;
    line-height: 1;
    margin-top: 2px;
  }
  .farm-scene {
    position: absolute;
    left: 0;
    top: 760px;
    width: 100%;
    height: 283px;
    background: linear-gradient(180deg, rgba(122,74,49,0) 0%, rgba(122,74,49,0.45) 40%, rgba(90,50,32,0.6) 100%);
  }
  .emblem {
    position: absolute;
    left: 114px;
    top: 652px;
    width: 244px;
    height: 244px;
  }
  .since {
    position: absolute;
    top: 641px;
    width: 100%;
    text-align: center;
    font-family: "Cinzel", serif;
    font-size: 13px;
    letter-spacing: 2px;
  }
  .ribbon {
    position: absolute;
    left: 100px;
    top: 862px;
    width: 272px;
    height: 38px;
  }
  .ribbon-text {
    position: absolute;
    left: 100px;
    top: 862px;
    width: 272px;
    line-height: 38px;
    text-align: center;
    font-family: "Oswald", sans-serif;
    font-weight: 500;
    font-size: 19px;
    letter-spacing: 0.5px;
  }
  .weight {
    position: absolute;
    top: 972px;
    width: 100%;
    text-align: center;
    font-family: "Cinzel", serif;
    font-size: 15px;
    color: var(--ink-dark);
  }
</style>
</head>
<body>
<main class="canvas">
  <article class="bag">
    <div class="seal-lines"><span></span><span></span><span></span></div>

    <header class="brand">
      <h1 class="brand-name">MORRELL</h1>
      <p class="brand-tagline">AUSTRALIAN COFFEE</p>
    </header>

    <h2 class="roast-name">
      <span class="line">ESPRESSO ROAST</span>
      <span class="form">BEANS</span>
    </h2>

    <div class="roast-level">MEDIUM ROAST</div>
    <div class="rule one"></div>
    <div class="rule two"></div>

    <p class="origin" style="margin:0">
      <span class="origin-label">PRODUCT MANUFACTURED</span>
      <span class="origin-country">AUSTRALIA</span>
    </p>

    <div class="farm-scene" role="img" aria-label="Line illustration of hillside coffee plantation rows and farmhouse"></div>

    <svg class="emblem" viewBox="0 0 244 244" aria-hidden="false">
      <circle cx="122" cy="122" r="116" fill="none" stroke="var(--ring-beige)" stroke-width="9"/>
      <circle cx="122" cy="122" r="100" fill="rgba(120,70,45,0.35)" role="img" aria-label="Map of Australia in white over plantation landscape"/>
    </svg>
    <div class="since">• SINCE 2016 •</div>

    <svg class="ribbon" viewBox="0 0 272 38" aria-hidden="true">
      <polygon points="0,4 272,4 262,19 272,34 0,34 10,19" fill="var(--ribbon)"/>
    </svg>
    <div class="ribbon-text">PREMIUM QUALITY COFFEE</div>

    <div class="weight">1 Kg</div>
  </article>
</main>
</body>
</html>
```